business card - Helicopter Flight Services, Flight School, etc.

We need a business card design for a new helicopter service.

We offer Helicopter Flight Services, Aerial Filming & Photography, Flight School, and Helicopter Tours. In that order.

Summit Bladecraft, Inc.
Harold Tessendy
SummitBladecraft@Lumenpost.com
303-555-0182

Based at the Coldbrook Airport in Van Nuys, CA. The final design should communicate integrity and safety. Pictures or logos at your discretion.

Card back side - surprise me.

```html
<!DOCTYPE html>
<html lang="en">
<head>
<meta charset="utf-8">
<title>Summit Bladecraft, Inc. — Business Card</title>
<link rel="stylesheet" href="https://fonts.googleapis.com/css2?family=Open+Sans:wght@400;600;700&display=swap">
<style>
  :root {
    --page-bg: #e9ecef;
    --card-white: #ffffff;
    --blue-deep: #0b4fa3;
    --blue-mid: #1a74c9;
    --blue-light: #3aa3df;
    --blue-pale: #8fcdf0;
    --ink-white: #ffffff;
    --muted-blue: #9cc6ee;
  }
  * { margin: 0; padding: 0; box-sizing: border-box; }
  html, body {
    width: 1200px; height: 913px; overflow: hidden;
    background: var(--page-bg);
    font-family: "Open Sans", Arial, sans-serif;
  }
  .stage {
    position: relative; width: 1200px; height: 913px;
    display: flex; align-items: center; justify-content: center; gap: 60px;
  }
  .card {
    position: relative; width: 520px; height: 297px;
    border-radius: 18px; overflow: hidden;
    box-shadow: 0 10px 28px rgba(0, 0, 0, 0.18);
  }
  /* Front */
  .card-front { background: var(--card-white); }
  .front-wave { position: absolute; inset: 0; width: 100%; height: 100%; }
  .brand {
    position: absolute; top: 28px; right: 36px;
    display: flex; align-items: center; gap: 10px;
    color: var(--blue-mid); font-weight: 700; font-size: 24px; letter-spacing: 0.5px;
  }
  .brand-dot {
    width: 20px; height: 20px; border-radius: 50%; background: var(--blue-mid);
  }
  .contact {
    position: absolute; left: 40px; bottom: 26px; color: var(--ink-white);
  }
  .contact-name { font-size: 20px; font-weight: 700; line-height: 1.3; }
  .contact-role { font-size: 13px; color: var(--muted-blue); margin: 0 0 8px; }
  .contact-line {
    display: flex; align-items: center; gap: 6px;
    font-size: 13px; line-height: 1.45;
  }
  .contact-line svg { width: 11px; height: 11px; flex: none; }
  /* Back */
  .card-back {
    background: linear-gradient(160deg, var(--blue-light) 0%, var(--blue-mid) 50%, var(--blue-deep) 100%);
    color: var(--ink-white);
  }
  .back-brand {
    position: absolute; top: 78px; left: 0; right: 0;
    display: flex; align-items: center; justify-content: center; gap: 12px;
    font-weight: 700; font-size: 24px;
  }
  .back-brand .brand-dot { background: var(--ink-white); }
  .services {
    position: absolute; top: 150px; left: 0; right: 0;
    text-align: center; list-style: none; font-size: 15px; line-height: 1.45;
  }
</style>
</head>
<body>
<main class="stage">
  <section class="card card-front" aria-label="Card front">
    <svg class="front-wave" viewBox="0 0 520 297" preserveAspectRatio="none" aria-hidden="true">
      <path d="M0 132 C150 104 330 164 520 72 L520 297 L0 297 Z" fill="var(--blue-pale)"/>
      <path d="M0 144 C150 116 330 176 520 84 L520 297 L0 297 Z" fill="var(--blue-light)"/>
      <path d="M0 156 C150 128 330 190 520 98 L520 297 L0 297 Z" fill="var(--blue-mid)"/>
      <path d="M0 170 C160 142 330 204 520 114 L520 297 L0 297 Z" fill="var(--blue-deep)"/>
    </svg>
    <div class="brand"><span class="brand-dot"></span><span>Summit Bladecraft, Inc.</span></div>
    <div class="contact">
      <p class="contact-name">Harold Tessendy</p>
      <p class="contact-role">Owner</p>
      <p class="contact-line">
        <svg viewBox="0 0 24 24" fill="var(--muted-blue)"><path d="M6.6 10.8a15 15 0 0 0 6.6 6.6l2.2-2.2c.3-.3.7-.4 1-.2 1.1.4 2.3.6 3.6.6.6 0 1 .4 1 1V20c0 .6-.4 1-1 1A17 17 0 0 1 3 4c0-.6.4-1 1-1h3.5c.6 0 1 .4 1 1 0 1.3.2 2.5.6 3.6.1.3 0 .7-.2 1z"/></svg>
        303-555-0182
      </p>
      <p class="contact-line">
        <svg viewBox="0 0 24 24" fill="none" stroke="var(--muted-blue)" stroke-width="2.5"><rect x="2" y="5" width="20" height="14" rx="2"/><path d="M2 6l10 7 10-7"/></svg>
        SummitBladecraft@Lumenpost.com
      </p>
    </div>
  </section>

  <section class="card card-back" aria-label="Card back">
    <div class="back-brand"><span class="brand-dot"></span><span>Summit Bladecraft, Inc.</span></div>
    <ul class="services">
      <li>Aerial Filming &amp; Photography</li>
      <li>Flight School</li>
      <li>Helicopter Tours (In that order)</li>
    </ul>
  </section>
</main>
</body>
</html>
```